PowerPoint Design Project

I need a Power Point slide template designed with 4 or 5 slides. We are a health care technology company and would like to take our current look and feel in this PP presentation to the next level and "prettied up"

Target Market(s)

Health Care Professionals

Industry/Entity Type

Health

Requirements
Must have
• Cannot change out the TOLVARE logo. The logo is all CAPS
Should not have
• The color blue is restricted and cannot be used.

```html
<!DOCTYPE html>
<html lang="en">
<head>
<meta charset="utf-8">
<title>Who we are — TOLVARE</title>
<link rel="stylesheet" href="https://fonts.googleapis.com/css2?family=Arimo:wght@400;700&display=swap">
<style>
  :root {
    --green: #adbb34;
    --green-deep: #9fae2c;
    --grey: #8e9093;
    --grey-light: #a3a5a8;
    --body: #6f7174;
    --white: #ffffff;
    --footer: #7a7c7f;
  }
  html, body {
    margin: 0;
    padding: 0;
    overflow: hidden;
    background: var(--white);
  }
  .slide {
    position: relative;
    width: 1200px;
    height: 900px;
    overflow: hidden;
    background: var(--white);
    font-family: "Arimo", Arial, sans-serif;
  }
  .feature-art {
    position: absolute;
    left: 565px;
    top: 0;
    width: 635px;
    height: 610px;
  }
  .feature-art svg { display: block; }
  .content {
    position: absolute;
    left: 62px;
    top: 172px;
    width: 478px;
  }
  .slide-title {
    margin: 0 0 22px;
    font-size: 43px;
    font-weight: 700;
    color: var(--grey);
    letter-spacing: -0.5px;
    line-height: 1.1;
  }
  .section-title {
    margin: 0 0 12px;
    font-size: 21px;
    font-weight: 700;
    color: var(--green);
    letter-spacing: -0.3px;
    line-height: 1.2;
  }
  .section + .section { margin-top: 34px; }
  .section p {
    margin: 0 0 14px;
    font-size: 11px;
    line-height: 13.3px;
    color: var(--body);
    letter-spacing: -0.45px;
  }
  .section p.gap { margin-top: 26px; }
  .footer {
    position: absolute;
    left: 0;
    right: 0;
    top: 834px;
    height: 40px;
  }
  .page-number {
    position: absolute;
    left: 33px;
    top: 0;
    width: 38px;
    height: 38px;
    border-radius: 50%;
    background: var(--green);
    color: var(--white);
    font-size: 14px;
    font-weight: 700;
    display: flex;
    align-items: center;
    justify-content: center;
  }
  .footer-note {
    position: absolute;
    left: 95px;
    top: 12px;
    font-size: 12.5px;
    color: var(--footer);
  }
  .footer-note .company { color: var(--green); font-weight: 700; }
  .footer-note .divider { margin: 0 6px; }
  .brand {
    position: absolute;
    right: 38px;
    top: 2px;
    display: flex;
    align-items: center;
    gap: 12px;
  }
  .brand-square {
    width: 30px;
    height: 30px;
    background: var(--green);
  }
  .brand-name {
    font-size: 32px;
    font-weight: 700;
    color: var(--grey);
    letter-spacing: 4px;
  }
</style>
</head>
<body>
<main class="slide">
  <div class="feature-art" role="img" aria-label="Large brand graphic in green and grey">
    <svg width="635" height="610" viewBox="0 0 635 610" xmlns="http://www.w3.org/2000/svg">
      <defs>
        <linearGradient id="greenTone" x1="0" y1="0" x2="1" y2="1">
          <stop offset="0" stop-color="#b4c23c"/>
          <stop offset="1" stop-color="#9fae2c"/>
        </linearGradient>
        <linearGradient id="greyTone" x1="0" y1="0" x2="1" y2="0">
          <stop offset="0" stop-color="#96989b"/>
          <stop offset="1" stop-color="#8a8c8f"/>
        </linearGradient>
      </defs>
      <rect x="85" y="0" width="550" height="100" fill="url(#greyTone)"/>
      <rect x="0" y="115" width="502" height="495" fill="url(#greenTone)"/>
      <rect x="517" y="115" width="118" height="470" fill="url(#greyTone)"/>
      <rect x="517" y="0" width="118" height="100" fill="url(#greenTone)"/>
    </svg>
  </div>

  <section class="content">
    <h1 class="slide-title">Who we are</h1>

    <div class="section">
      <h2 class="section-title">About Lorem</h2>
      <p>Lorem ipsum dolor sit amet, consectetuer adipiscing elit. Aenean commodo ligula eget dolor. Aenean massa. Cum sociis natoque penatibus et magnis dis parturient montes, nascetur ridiculus mus.</p>
      <p>Donec quam felis, ultricies nec, pellentesque eu, pretium quis, sem. Nulla consequat massa quis enim. Donec pede justo, fringilla vel, aliquet nec, vulputate eget, arcu.</p>
      <p class="gap">In enim justo, rhoncus ut, imperdiet a, venenatis vitae, justo. Nullam dictum felis eu pede mollis pretium. Integer tincidunt. Cras dapibus. Vivamus elementum semper nisi. Aenean vulputate eleifend tellus. Aenean leo ligula, porttitor eu, consequat vitae, eleifend ac, enim. Aliquam lorem ante, dapibus in, viverra quis, feugiat a</p>
    </div>

    <div class="section">
      <h2 class="section-title">Mision Lorem</h2>
      <p>LLorem ipsum dolor sit amet, consectetuer adipiscing elit. Aenean commodo ligula eget dolor. Aenean massa. Cum sociis natoque penatibus et magnis dis parturient montes, nascetur ridiculus mus.</p>
      <p>Donec quam felis, ultricies nec, pellentesque eu, pretium quis, sem. Nulla consequat massa quis enim. Donec pede justo, fringilla vel, aliquet nec, vulputate eget, arcu.</p>
      <p>In enim justo, rhoncus ut, imperdiet a, venenatis vitae, justo. Nullam dictum felis eu pede mollis pretium. Integer tincidunt. Cras dapibus. Vivamus elementum semper nisi. Aenean vulputate eleifend tellus. Aenean leo ligula, porttitor eu, consequat vitae, eleifend ac, enim. Aliquam lorem ante, dapibus in, viverra quis, feugiat a</p>
    </div>
  </section>

  <footer class="footer">
    <div class="page-number">2</div>
    <div class="footer-note"><span class="company">TOLVARE Network Inc</span><span class="divider">|</span>Company Confidential</div>
    <div class="brand">
      <span class="brand-square" aria-hidden="true"></span>
      <span class="brand-name">TOLVARE</span>
    </div>
  </footer>
</main>
</body>
</html>
```